NZ First of it's kind solutions directory and marketplace for busy Mums needs a business card design

We need a business card design for our new nationwide business in NZ (long term plans to go global). We provide solutions to the everyday challenges that busy Mums face by connecting them with quality communities and suppliers of carefully selected, relevant products and services. We sell direct via our online marketplace. The final design should communicate our values of inclusivity, quality and smart solutions. Colours should incorporate our logo colour palette of #477077 and #6ba8b2. Our website is at https://www.brightnestly.com

Target Market(s)

busy Mums, Age 28 – 50, female, income over $100K, location main centres NZ primarily but NZ wide. Is likely juggling work or career with a young family. Probably had hobbies which have fallen by the wayside.
-Wants to succeed in her chosen career without compromising on family life
-to successfully juggle her career without feeling like she is compromising her children
- Is time poor, something always has to give and it’s generally her health (she’ll stay up late, get stressed)
- probably ex corporate or professional career. Has discretional income

Industry/Entity Type

Business

Contact Information for Business Card

Jodie Farnsworth, Founder, BrightNestly.com (Strapline Browse; Pick; Sorted), 48 Kowhai Terrace, Hillsborough, Auckland 1058, New Zealand. Mob: 021 437 518 Ph: +64 (0)9 584 7163

Font styles to use
Other font styles liked:
• Raleway, and/or Architects Daughter

Colors
00a990
33b8a4
86cfc6
cfeae6

Requirements
Must have
• the above details, streamline. the logo and colours associated with those logos
Should not have
• foil or metallic colours

```html
<!DOCTYPE html>
<html lang="en">
<head>
<meta charset="utf-8">
<title>BrightNestly – Business Card</title>
<link rel="stylesheet" href="https://fonts.googleapis.com/css2?family=Architects+Daughter&family=Raleway:wght@400;500;700&display=swap">
<style>
  :root {
    --backdrop: #0d5f5a;
    --card: #d2ebe7;
    --brand-dark: #477077;
    --brand-deep: #3a7570;
    --accent: #33b8a4;
    --accent-soft: #2fa796;
  }
  * { box-sizing: border-box; margin: 0; padding: 0; }
  html, body { width: 1200px; height: 1000px; overflow: hidden; }
  body {
    background: var(--backdrop);
    position: relative;
    font-family: "Raleway", sans-serif;
  }
  .card {
    position: absolute;
    left: 220px;
    width: 786px;
    height: 448px;
    background: var(--card);
  }
  .card--front { top: 39px; }
  .card--back { top: 505px; text-align: center; }

  .brand {
    position: absolute;
    left: 52px;
    top: 150px;
    display: flex;
    align-items: center;
    gap: 34px;
  }
  .brand__dot {
    width: 84px; height: 84px;
    border-radius: 50%;
    background: var(--brand-dark);
    flex: none;
  }
  .brand__name {
    font-family: "Raleway", sans-serif;
    font-weight: 700;
    font-size: 82px;
    letter-spacing: -1px;
    color: var(--brand-dark);
    line-height: 1;
  }
  .tagline {
    position: absolute;
    left: 280px;
    top: 242px;
    font-family: "Architects Daughter", cursive;
    font-size: 28px;
    color: var(--brand-deep);
  }

  .back__dot {
    display: block;
    width: 42px; height: 42px;
    border-radius: 50%;
    background: var(--brand-dark);
    margin: 46px auto 0;
  }
  .person__name {
    margin-top: 30px;
    font-family: "Architects Daughter", cursive;
    font-size: 50px;
    letter-spacing: 2px;
    color: var(--brand-deep);
    line-height: 1.1;
    text-transform: uppercase;
  }
  .person__role {
    margin-top: 6px;
    font-size: 27px;
    color: var(--accent);
    letter-spacing: 1px;
  }
  .site {
    margin-top: 42px;
    font-size: 29px;
    font-weight: 700;
    color: var(--brand-dark);
  }
  .strapline {
    margin-top: 4px;
    font-size: 23px;
    color: var(--accent);
  }
  .address {
    margin-top: 40px;
    font-size: 22px;
    color: var(--accent-soft);
  }
  .phones {
    margin-top: 12px;
    font-size: 22px;
    color: var(--accent-soft);
  }
  .phones span + span { margin-left: 26px; }
  .phones b { font-weight: 700; color: var(--accent-soft); }
</style>
</head>
<body>
  <section class="card card--front">
    <div class="brand">
      <span class="brand__dot"></span>
      <span class="brand__name">BrightNestly</span>
    </div>
    <p class="tagline">Solutions for Busy Mums.</p>
  </section>

  <section class="card card--back">
    <span class="back__dot"></span>
    <h1 class="person__name">Jodie Farnsworth</h1>
    <p class="person__role">FOUNDER</p>
    <p class="site">BrightNestly.com</p>
    <p class="strapline">Browse, Pick, Sorted</p>
    <p class="address">48 Kowhai Terrace, Hillsborough, Auckland 1058, New Zealand</p>
    <p class="phones"><span><b>M:</b> 021 437 518</span><span><b>P:</b> +64 (0)9 584 7163</span></p>
  </section>
</body>
</html>
```